Need Trifold Brochure

I need a trifold brochure asap for a project.

Please KNOW how to do a trifold brochure. It should be an 8 1/2 x 11 brochure that is folded in thirds. So there are ultimately 6 sections, 3 on the front and 3 on the back. We need content on both sides, not just one. If you aren't sure what a trifold is please google it. If you submit a design that is not a true trifold it will be immediately eliminated.

All content located on this page
http://harborviewaestheticclinic.example/
All text on this page needs to be incorporated.

Also I attached the 3 before and after images. All 3 of these need to be incorporated preferable\y on the inside of the trifold on per page. The very BACK of the trifold doesn't have to have content, other than maybe the company and phone.

On the outside of the trifold (not the inside) you could do a muted sea or ocean scape as long as the text is legible.

Same colors as website.

Reason: Meant to put 7 days

Target Market(s)

See website. This is for face lifts, so mostly women age 40 and over.

Industry/Entity Type

It Company

Requirements
Must have
• All content located on this page

Also I attached the 3 before and after images. When the trifold is open these could be on each of the 3 pages of the trifold, preferably at the top.

Same colors as website.

```html
<!DOCTYPE html>
<html lang="en">
<head>
<meta charset="utf-8">
<title>The Evergreen Facelift – Trifold Brochure</title>
<link href="https://fonts.googleapis.com/css2?family=PT+Sans+Narrow:wght@700&family=Source+Sans+3:wght@400;600;700&display=swap" rel="stylesheet">
<style>
  :root {
    --backdrop: #2a2a2a;
    --paper: #ffffff;
    --sky-blue: #84b4f6;
    --orange: #ff7a2a;
    --navy: #1f2d9c;
    --ink: #1b1b1b;
    --link-blue: #1f2d9c;
    --bullet: #8fb4ef;
    --photo-top: #3f7fd0;
    --photo-bottom: #b9d0ea;
  }
  * { box-sizing: border-box; margin: 0; padding: 0; }
  html, body { width: 1200px; height: 1000px; overflow: hidden; }
  body {
    background: var(--backdrop);
    position: relative;
    font-family: "Source Sans 3", "Myriad Pro", sans-serif;
    color: var(--ink);
  }
  .brochure {
    position: absolute; left: 20px; top: 40px;
    width: 1157px; height: 817px;
    background: var(--paper);
    box-shadow: 0 6px 16px rgba(0,0,0,.5);
    overflow: hidden;
  }
  .panel { position: absolute; top: 0; height: 817px; }
  .panel--inside { left: 0; width: 380px; }
  .panel--back { left: 380px; width: 392px; }
  .panel--cover { left: 772px; width: 385px; }

  /* Inside panel */
  .offers-header {
    position: absolute; left: 0; top: 0; width: 380px; height: 105px;
    background: var(--sky-blue); overflow: hidden;
  }
  .offers-header h2 {
    position: absolute; left: 40px; top: 54px;
    font-family: "Source Sans 3", sans-serif; font-weight: 700;
    font-size: 62px; line-height: 1; color: #fff; letter-spacing: -0.5px;
  }
  .offer-list { position: absolute; left: 44px; top: 122px; width: 330px; list-style: none; }
  .offer-list li {
    position: relative; padding-left: 22px;
    font-size: 15px; line-height: 22px; margin-bottom: 9.6px;
    white-space: nowrap;
  }
  .offer-list li::before {
    content: ""; position: absolute; left: 2px; top: 7px;
    width: 8px; height: 8px; background: var(--bullet);
    transform: rotate(45deg);
  }
  .offer-list .hl { color: var(--orange); font-weight: 700; }
  .tagline {
    position: absolute; left: 0; top: 564px; width: 380px; text-align: center;
    color: var(--orange); font-weight: 700; font-size: 18px; line-height: 25px;
  }
  .price-band {
    position: absolute; left: 0; top: 627px; width: 380px; height: 49px;
    background: var(--orange); color: #fff; text-align: center;
    font-weight: 700; text-shadow: 1px 2px 2px rgba(0,0,0,.45);
  }
  .price-band .label { font-size: 18px; vertical-align: middle; }
  .price-band .amount { font-size: 36px; line-height: 49px; vertical-align: middle; margin-left: 4px; }
  .call-block {
    position: absolute; left: 0; top: 676px; width: 380px; height: 141px;
    background: var(--sky-blue); text-align: center;
    font-size: 18px; line-height: 23px; padding-top: 17px; text-transform: uppercase;
  }
  .call-block .phone { color: var(--link-blue); font-weight: 700; font-size: 20px; }

  /* Back panel */
  .back-title {
    position: absolute; left: 34px; top: 626px;
    font-family: "PT Sans Narrow", sans-serif; font-weight: 700;
    font-size: 31px; color: var(--orange);
  }
  .contact { position: absolute; left: 34px; top: 668px; font-size: 15px; line-height: 22px; font-style: normal; }
  .back-band { position: absolute; left: 0; bottom: 0; width: 392px; height: 33px; background: var(--navy); }

  /* Cover */
  .cover-photo {
    position: absolute; left: 0; top: 0; width: 385px; height: 730px;
    background: linear-gradient(180deg, var(--photo-top) 0%, var(--photo-bottom) 100%);
  }
  .cover-title {
    position: absolute; left: 0; top: 46px; width: 385px; text-align: center;
    font-family: "PT Sans Narrow", sans-serif; font-weight: 700;
    font-size: 38px; color: #fff;
  }
  .cover-sub {
    position: absolute; left: 0; top: 101px; width: 385px; text-align: center;
    color: #fff; font-weight: 700; font-size: 18px; line-height: 25px;
  }
  .cover-strip { position: absolute; left: 0; top: 730px; width: 385px; height: 11px; background: var(--navy); }
  .cover-footer {
    position: absolute; left: 0; top: 741px; width: 385px; height: 76px;
    background: var(--sky-blue); text-align: center; color: #fff;
  }
  .cover-footer .call { font-weight: 700; font-size: 24px; padding-top: 5px; line-height: 30px; }
  .cover-footer .web { color: var(--ink); font-weight: 700; font-size: 14px; margin-top: 4px; }
</style>
</head>
<body>
  <main class="brochure">
    <section class="panel panel--inside">
      <div class="offers-header"><h2>Offers</h2></div>
      <ul class="offer-list">
        <li><span class="hl">No</span> General Anesthesia<br>(but available as an option if desired)</li>
        <li><span class="hl">Decreased</span> Risks</li>
        <li><span class="hl">Less</span> Scars</li>
        <li><span class="hl">Very Quick</span> Recovery*</li>
        <li><span class="hl">Less</span> Bruising and Swelling*</li>
        <li><span class="hl">Significant</span> Improvement*</li>
        <li><span class="hl">No</span> Need for Special Post-Op Care</li>
        <li><span class="hl">Short</span> Surgery Time</li>
        <li><span class="hl">Free</span> Consultation With Our Staff</li>
        <li>Surgery performed by a fully ABPS<br>Board Certified, internationally<br>known, plastic surgeon.</li>
        <li>Optional add-on procedures can be<br>done at the same time.</li>
      </ul>
      <p class="tagline">The new way to look<br>and feel better fast for less!</p>
      <div class="price-band"><span class="label">TOTAL COST</span><span class="amount">$4500</span></div>
      <div class="call-block">
        Call&nbsp; <span class="phone">310-555-0147</span><br>
        Today for an appointment<br>
        in Santa Monica<br>
        Harborview Aesthetic Clinic
      </div>
    </section>

    <section class="panel panel--back">
      <h3 class="back-title">The Evergreen Facelift</h3>
      <address class="contact">
        Address, ABC Street<br>
        XYZ lane, 123 , Londan, UK<br>
        T : 310-555-0147<br>
        E :&nbsp; hello@harborview.example<br>
        W : www. harborviewaestheticclinic.example
      </address>
      <div class="back-band"></div>
    </section>

    <section class="panel panel--cover">
      <div class="cover-photo" role="img" aria-label="Muted seascape photo: blue sky with wispy clouds over calm water and a distant shoreline"></div>
      <h1 class="cover-title">The Evergreen Facelift</h1>
      <p class="cover-sub">The new way to look<br>and feel better fast for less!</p>
      <div class="cover-strip"></div>
      <div class="cover-footer">
        <p class="call">Call : 310-555-0147</p>
        <p class="web">www. harborviewaestheticclinic.example</p>
      </div>
    </section>
  </main>
</body>
</html>
```